Lou Brannigan Party invite for 8/20/2018

Lou Brannigan is returning to downtown Jacksonport for another night of fun at Twelve Past Anywhere. Bring a date and tell your friends! Monday, August 20, 2018.
The party starts at 7 pm with limo rides home starting at 11:30.

Target Market(s)

our friends- we will be mailing out this invite

Colors

Designer to choose colors to be used in the design.

Requirements
Must have
• 2 sided postcard for mailing invite
Nice to have
• fun party layout- use the images provides and whatever else you think

```html
<!DOCTYPE html>
<html lang="en">
<head>
<meta charset="utf-8">
<title>Lou Brannigan Party Invite Postcard</title>
<link href="https://fonts.googleapis.com/css2?family=Lato:wght@400;700;900&family=Yellowtail&display=swap" rel="stylesheet">
<style>
  :root {
    --backdrop: #a9a9a9;
    --banner-red: #b3262b;
    --accent-red: #c41f26;
    --paper: #f1efe9;
    --ink: #141414;
    --white: #ffffff;
    --photo-dark: #1c1410;
    --photo-warm: #b98a4e;
  }
  * { margin: 0; padding: 0; box-sizing: border-box; }
  html, body {
    width: 1200px; height: 962px; overflow: hidden;
    background: var(--backdrop);
  }
  .canvas {
    position: relative; width: 1200px; height: 962px;
    display: flex; flex-direction: column; align-items: center;
    justify-content: center; gap: 28px;
  }
  .postcard {
    position: relative; width: 660px; height: 440px; overflow: hidden;
    box-shadow: 0 6px 18px rgba(0,0,0,.25);
  }

  /* Front */
  .front { background: var(--photo-dark); }
  .front__photo {
    position: absolute; inset: 0;
    background:
      radial-gradient(ellipse at 30% 72%, rgba(226,180,110,.85) 0%, rgba(160,110,60,.5) 30%, transparent 55%),
      linear-gradient(180deg, #6d6f86 0%, #241c18 28%, #1a120e 60%, #4a3020 100%);
  }
  .front__shapes { position: absolute; inset: 0; }
  .front__banner-text {
    position: absolute; left: 300px; top: 30px; width: 320px;
    text-align: center; color: var(--white);
    font-family: "Lato", sans-serif;
  }
  .name-script {
    font-family: "Yellowtail", cursive; font-weight: 400;
    line-height: .9; color: var(--white);
  }
  .front .name-script__first { font-size: 72px; display: block; }
  .front .name-script__last { font-size: 64px; display: block; margin-top: -4px; }
  .front__lead { font-size: 17px; margin-top: 16px; line-height: 1.1; }
  .front__town { font-size: 18px; font-weight: 700; letter-spacing: .5px; }
  .front__rule { width: 220px; height: 2px; background: var(--white); margin: 10px auto 8px; }
  .front__night { font-size: 17px; line-height: 1.15; }
  .front__venue { font-size: 17px; font-weight: 700; }
  .front__cta {
    position: absolute; left: 290px; top: 356px; width: 360px;
    text-align: center; color: var(--accent-red); font-family: "Lato", sans-serif;
  }
  .front__cta-line { font-size: 15px; font-weight: 700; }
  .front__date { font-size: 20px; font-weight: 900; margin-top: 2px; }

  /* Back */
  .back { background: var(--paper); color: var(--ink); font-family: "Lato", sans-serif; }
  .back__details { position: absolute; left: 40px; top: 50px; width: 280px; text-align: center; }
  .back .name-script { color: var(--ink); }
  .back .name-script__first { font-size: 60px; display: block; }
  .back .name-script__last { font-size: 54px; display: block; margin-top: -4px; }
  .back__lead { font-size: 14px; font-weight: 700; margin-top: 12px; line-height: 1.1; }
  .back__rule { width: 220px; height: 2px; background: var(--ink); margin: 7px auto; }
  .back__line { font-size: 14px; font-weight: 700; line-height: 1.15; }
  .back__stamp {
    position: absolute; right: 40px; top: 40px; width: 86px; height: 62px;
    border: 1.5px solid var(--ink);
  }
  .back__address { position: absolute; left: 370px; top: 230px; width: 250px; }
  .back__address-line { height: 1.5px; background: #555; margin-bottom: 38px; }
</style>
</head>
<body>
<main class="canvas">

  <section class="postcard front" aria-label="Postcard front">
    <div class="front__photo" role="img" aria-label="Photo of the singer performing with a guitar on a lit outdoor wooden stage at dusk, crowd at the right"></div>
    <svg class="front__shapes" width="660" height="440" viewBox="0 0 660 440" aria-hidden="true">
      <polygon points="300,0 620,0 620,300 460,345 300,300" fill="var(--banner-red)" opacity=".93"/>
      <polygon points="270,290 460,345 660,290 660,440 255,440" fill="var(--white)" opacity=".78"/>
    </svg>
    <div class="front__banner-text">
      <h1 class="name-script"><span class="name-script__first">Lou</span><span class="name-script__last">Brannigan</span></h1>
      <p class="front__lead">is returning to downtown</p>
      <p class="front__town">JACKSONPORT</p>
      <div class="front__rule"></div>
      <p class="front__night">Another Night Of Fun At</p>
      <p class="front__venue">Twelve Past Anywhere</p>
    </div>
    <div class="front__cta">
      <p class="front__cta-line">Bring a date and tell your friends!</p>
      <p class="front__date">Monday, August 20, 2018.</p>
    </div>
  </section>

  <section class="postcard back" aria-label="Postcard back">
    <div class="back__details">
      <h2 class="name-script"><span class="name-script__first">Lou</span><span class="name-script__last">Brannigan</span></h2>
      <p class="back__lead">is returning to downtown<br>JACKSONPORT</p>
      <div class="back__rule"></div>
      <p class="back__line">Another Night Of Fun At<br>Twelve Past Anywhere</p>
      <div class="back__rule"></div>
      <p class="back__line">Party starts at 7 pm with<br>limo rides home starting<br>at 11:30.</p>
    </div>
    <div class="back__stamp"></div>
    <div class="back__address">
      <div class="back__address-line"></div>
      <div class="back__address-line"></div>
      <div class="back__address-line"></div>
    </div>
  </section>

</main>
</body>
</html>
```